Lumivex - Stationary Design

We need a stationary set designed including a logo, business cards, envelopes, letterhead, brochure, etc for our new company "luMivex". We are a business development firm specializing in local marketing solutions. We utilize modern marketing technologies to craft unique marketing strategies that meet our client's needs. Our main products are mobile technologies including sms marketing, mobile websites, bluetooth marketing, and social wifi, but we will also provide other digital marketing solutions such as website design, social media consulting, email marketing, etc.

The design set should incorporate blue and grey color(s), communicate professionalism, and modern technology. Please also feel free to use our current tagline "Steady Local Reach Plans" or feel free to craft a new one of your own.

The contact info is as follows:
2374 Orchard Ln.
Brenmoor, NC 28714

Phone 704-913-6248
email:derek@lumivexplanning.com

Please be very creative and let me know if you have any questions!!

There will be future opportunities for the winner!!

Update: A few minor changes:

1. We will be using only the name "lumivex" not strategy.

2. Please use the tagline: Steady Local Reach Plans

Please make those changes to your design.

Thanks

I want to provide a few links for inspiration as well:

Target Market(s)

Small businesses including restaurants, hotels, car lots, doctors, dentists, etc.

Industry/Entity Type

Marketing

```html
<!DOCTYPE html>
<html lang="en">
<head>
<meta charset="utf-8">
<title>luMivex — Business Cards</title>
<link rel="stylesheet" href="https://fonts.googleapis.com/css2?family=Open+Sans:wght@400;600&display=swap">
<style>
  :root {
    --page-bg: #ececec;
    --card-white: #fbfbfb;
    --brand-blue: #1f7fc2;
    --blue-deep: #1d5fae;
    --blue-mid: #2b8fd0;
    --blue-light: #8fcbef;
    --ink-grey: #3a3d42;
    --soft-grey: #7b8087;
    --band-white: rgba(240, 244, 248, 0.9);
  }
  * { box-sizing: border-box; margin: 0; padding: 0; }
  html, body {
    width: 1200px; height: 863px; overflow: hidden;
    background: var(--page-bg);
    font-family: "Open Sans", Arial, sans-serif;
  }
  .canvas { position: relative; width: 1200px; height: 863px; }

  .card {
    position: absolute; top: 288px;
    width: 500px; height: 286px;
    overflow: hidden;
    box-shadow: 0 6px 18px rgba(0,0,0,0.12);
  }
  .card--front { left: 80px; background: var(--blue-mid); }
  .card--back { left: 620px; background: var(--card-white); }

  /* Front card */
  .front-artwork { position: absolute; inset: 0; width: 100%; height: 100%; }
  .info-band {
    position: absolute; left: 0; top: 74px;
    width: 452px; height: 92px;
    background: var(--band-white);
    display: flex; align-items: center;
    padding-left: 34px;
  }
  .info-band__name {
    font-size: 27px; font-weight: 600; color: var(--ink-grey);
    letter-spacing: 0.2px;
  }
  .info-band__divider {
    width: 2px; height: 58px; background: var(--brand-blue);
    margin: 0 16px 0 22px;
  }
  .info-band__details { font-size: 12.5px; line-height: 1.5; color: var(--ink-grey); white-space: nowrap; }
  .info-band__label { font-weight: 600; }

  /* Back card */
  .back-decoration {
    position: absolute; right: -40px; top: 70px;
    width: 260px; height: 260px; border-radius: 50%;
    background: radial-gradient(circle, rgba(210,212,216,0.55) 0%, rgba(225,227,230,0.25) 55%, rgba(251,251,251,0) 72%);
  }
  .brand { position: absolute; left: 34px; top: 32px; display: flex; align-items: center; }
  .brand__dot {
    width: 34px; height: 34px; border-radius: 50%;
    background: var(--brand-blue); margin-right: 10px;
  }
  .brand__name { font-size: 30px; font-weight: 600; color: var(--ink-grey); line-height: 1; }
  .brand__tagline {
    position: absolute; left: 78px; top: 70px;
    font-size: 11px; color: var(--brand-blue);
  }
  .contact-person {
    position: absolute; left: 34px; top: 108px;
    border-left: 3px solid var(--brand-blue);
    padding-left: 8px;
    font-size: 12.5px; font-weight: 600; color: var(--brand-blue);
  }
  .services {
    position: absolute; left: 34px; top: 138px;
    display: flex; gap: 44px;
  }
  .services__group {
    border-left: 2px solid var(--brand-blue);
    padding-left: 8px;
    font-size: 12.5px; line-height: 1.5; color: var(--soft-grey);
  }
</style>
</head>
<body>
<main class="canvas">

  <section class="card card--front" aria-label="Business card front">
    <svg class="front-artwork" viewBox="0 0 500 286" preserveAspectRatio="none"
         role="img" aria-label="Abstract flowing blue ribbon artwork">
      <defs>
        <linearGradient id="frontWash" x1="0" y1="0" x2="1" y2="1">
          <stop offset="0" stop-color="#7cc3ee"/>
          <stop offset="0.45" stop-color="#2b8fd0"/>
          <stop offset="1" stop-color="#1d5fae"/>
        </linearGradient>
      </defs>
      <rect width="500" height="286" fill="url(#frontWash)"/>
    </svg>

    <div class="info-band">
      <span class="info-band__name">luMivex</span>
      <span class="info-band__divider"></span>
      <p class="info-band__details">
        2374 Orchard Ln. Brenmoor, NC 28714<br>
        <span class="info-band__label">Phone</span> : 704-913-6248<br>
        <span class="info-band__label">Email</span> : derek@lumivexplanning.com
      </p>
    </div>
  </section>

  <section class="card card--back" aria-label="Business card back">
    <div class="back-decoration" role="img" aria-label="Faint grey decorative shape"></div>

    <div class="brand">
      <span class="brand__dot"></span>
      <span class="brand__name">luMivex</span>
    </div>
    <p class="brand__tagline">Steady Local Reach Plans</p>

    <p class="contact-person">Mara Quill +91 40718 52936</p>

    <div class="services">
      <p class="services__group">Email Marketing<br>Digital Marketing</p>
      <p class="services__group">Website Design<br>Social Media Consulting</p>
    </div>
  </section>

</main>
</body>
</html>
```